Word template for IT training materials

What is needed is a Word template for training materials. It is needed for training materials for IT seminars. The template should include: - Title page / Cover sheet - Notes on the version (version history, ...) - Table of contents - Texts - Templates for notes of seminar participants - Design for notes, warnings, and important information - Duplex printing as well as one-sided should be provided - List of Figures Above all, the design is important. Text layout would be desirable but is 2nd prio. The template should look good in both color and black and white. The design should be based on the existing documents (logo, letter paper, envelope). (See attachement). The design should be modern, minimalist but professional. It should be based on the coloring of the existing documents. The design does not necessarily have to be based on it. ENGLISH TRANSLATION: What is needed is a Word template for training materials. It is needed for training materials for IT seminars. The template should include: - Title page / cover page - Release Notes - Table of Contents - Text - Templates for notes of seminar participants - Design for hints, warnings, and important information - Duplex printing as well as one-sided should be provided - List of Figures Above, the design is important. Text layout would be desirable but is 2nd prio. The template should look good in both color and black and white. The design should be based on the existing documents (logo, letter paper, envelope). (Lake attachement). The design should be modern, minimalist but professional. It should be based on the coloring of the existing documents. The design does not necessarily have to be based on it.

Target Market(s)

Training materials, seminars for IT professionals ENGLISH TRANSLATION: Training materials, seminars for IT professionals

Industry/Entity Type

Consulting

Font styles to use
Serif
Sans Serif

Colors

Designer to choose colors to be used in the design.

Requirements
Must have
• - Cover page (seminar topic, logo, date, ....) -> Cover sheet should include: * Logo * Inscription: Consultation and training * Name * Address and contact details: * Tel. 49 (0) 83 17/4 26 71 - 38 * Fax. 49 (0) 83 17/52 94 * Mobile: 49 (0) 160 427 18 36 * Mail: info@lanzer-korbin.example * Topic of the seminar - comments on the version (version history, ...) - Table of Contents - Texts - Templates for notes of seminar participants - Design for notes, warnings, and important information - Duplex printing as well as one-sided should be provided - Header and footer - List of figures ENGLISH TRANSLATION: - Title page / cover sheet (seminar topic, logo, date, .. ..) -> Cover sheet should include: * Logo * Inscription: Consultation and Training * Name * Address and contact details: * Phone 49 (0) 83 17/4 26 71 - 38 * Fax. 49 (0) 83 17/52 94 * Mobile: 49 (0) 160 427 18 36 * Mail: info @ lanzer-korbin. example * Seminar Theme - Title page / cover page - Release Notes - Table of Contents - Text - Templates for notes of seminar participants - Design for hints, warnings, and important information - Duplex printing as well as one-sided should be provided - List of Figures
Should not have
• - too much color - too much color

```html
<!DOCTYPE html>
<html lang="de">
<head>
<meta charset="utf-8">
<title>Schulungsunterlagen für IT-Seminare – Vorlage</title>
<link rel="stylesheet" href="https://fonts.googleapis.com/css2?family=Nunito:wght@300;400;700;800&family=Roboto:wght@300;400;700&family=Pinyon+Script&display=swap">
<style>
  :root {
    --blue: #1f63ad;
    --navy: #133f7c;
    --deep: #0c2b5c;
    --sky: #3d96d6;
    --teal: #2aa6c8;
    --ink: #3a3f47;
    --grey: #6b7079;
    --paper: #ffffff;
  }
  * { box-sizing: border-box; margin: 0; padding: 0; }
  html, body { width: 1200px; height: 4255px; overflow: hidden; background: var(--paper); }
  body { position: relative; font-family: "Roboto", Arial, sans-serif; color: var(--ink); }
  .abs { position: absolute; }

  /* ---------- cover page ---------- */
  .cover { position: absolute; left: 0; top: 0; width: 1200px; height: 1702px; overflow: hidden; background: var(--paper); }
  .brand { position: absolute; display: flex; flex-direction: column; align-items: center; }
  .brand-mark { border-radius: 50%; background: radial-gradient(circle at 35% 30%, var(--sky), var(--navy)); }
  .brand-name { font-family: "Nunito", Arial, sans-serif; font-weight: 800; color: var(--blue); text-transform: uppercase; letter-spacing: 2px; text-align: center; line-height: 1.05; }
  .cover .brand { left: 95px; top: 170px; width: 280px; }
  .cover .brand-mark { width: 190px; height: 190px; }
  .cover .brand-name { font-size: 40px; margin-top: 20px; }

  .doc-kicker { position: absolute; left: 700px; top: 192px; width: 350px; text-align: center; font-family: "Nunito", sans-serif; font-size: 30px; color: var(--blue); letter-spacing: 1px; }
  .doc-title { position: absolute; left: 520px; top: 238px; width: 530px; text-align: center; font-family: "Nunito", sans-serif; font-weight: 800; font-size: 56px; line-height: 1.1; color: var(--blue); }

  .slogan { position: absolute; left: 0; top: 520px; width: 1200px; text-align: center; font-family: "Nunito", sans-serif; font-weight: 300; font-size: 76px; color: #5b6068; }
  .slogan strong { font-weight: 700; color: #4b5058; }
  .slogan-copy { position: absolute; left: 110px; top: 628px; width: 990px; font-size: 13px; line-height: 1.45; color: var(--grey); }

  .hero-art { position: absolute; left: 150px; top: 730px; width: 900px; height: 700px; border-radius: 12px; background: linear-gradient(160deg, #eef3f8 0%, #dfe7ef 60%, #cfd9e4 100%); }

  .cover-wave { position: absolute; left: 0; top: 1230px; }
  .cover-block { position: absolute; left: 30px; top: 1330px; width: 920px; color: #fff; }
  .cover-block h2 { font-family: "Nunito", sans-serif; font-weight: 800; font-size: 58px; line-height: 1; letter-spacing: 1px; }
  .cover-block .sub { font-family: "Nunito", sans-serif; font-weight: 300; font-size: 40px; letter-spacing: 2px; line-height: 1.1; }
  .cover-block h3 { font-family: "Nunito", sans-serif; font-weight: 800; font-size: 26px; margin-top: 20px; letter-spacing: .5px; }
  .cover-block .lead { font-size: 14px; line-height: 1.45; margin-top: 8px; opacity: .92; }
  .cover-block .body { font-size: 13px; line-height: 1.45; margin-top: 16px; opacity: .85; width: 900px; }

  /* ---------- contents page ---------- */
  .contents { position: absolute; left: 0; top: 1730px; width: 1200px; height: 1620px; overflow: hidden; background: var(--paper); }
  .contents .brand { left: 110px; top: 85px; flex-direction: row; gap: 22px; }
  .contents .brand-mark { width: 150px; height: 150px; box-shadow: 0 6px 14px rgba(0,0,0,.25); }
  .contents .brand-name { font-size: 26px; text-align: center; }

  .toc-title { position: absolute; left: 110px; top: 320px; font-family: "Pinyon Script", cursive; font-weight: 400; font-size: 72px; color: var(--blue); }

  .section-art { position: absolute; left: 113px; top: 505px; width: 312px; height: 320px; border-radius: 10px; background: linear-gradient(150deg, #f1f4f8, #d7e0ea); }
  .section-rule { position: absolute; left: 468px; top: 520px; width: 3px; height: 400px; background: #9aa0a8; }
  .section-head { position: absolute; left: 510px; top: 525px; font-family: "Nunito", sans-serif; font-weight: 400; font-size: 31px; color: #555a62; letter-spacing: .5px; }
  .section-text { position: absolute; left: 510px; top: 578px; width: 600px; font-size: 12.5px; line-height: 1.3; color: var(--grey); text-align: justify; }

  .topic { position: absolute; top: 985px; width: 300px; }
  .topic-icon { width: 100px; height: 100px; border-radius: 50%; margin-left: 45px; }
  .topic h4 { font-family: "Roboto", sans-serif; font-weight: 700; font-size: 15px; color: #4b5058; margin-top: 22px; }
  .topic p { font-size: 14px; line-height: 1.35; color: var(--grey); margin-top: 4px; }

  .tag { position: absolute; color: #fff; font-family: "Nunito", sans-serif; font-weight: 800; display: flex; align-items: center; justify-content: center; letter-spacing: .5px; white-space: nowrap; }
  .tag-teal { left: 653px; top: 1235px; width: 510px; height: 90px; background: var(--teal); font-size: 38px; }
  .tag-navy { left: 497px; top: 1330px; width: 666px; height: 80px; background: var(--navy); font-size: 30px; box-shadow: 0 4px 8px rgba(0,0,0,.2); }
</style>
</head>
<body>

<!-- ================= COVER PAGE ================= -->
<section class="cover">
  <svg class="abs" style="left:0;top:0" width="1200" height="110" viewBox="0 0 1200 110">
    <defs>
      <linearGradient id="topBand" x1="0" y1="0" x2="1" y2="0">
        <stop offset="0" stop-color="#2f7fc6"/>
        <stop offset=".55" stop-color="#1f63ad"/>
        <stop offset="1" stop-color="#0c2b5c"/>
      </linearGradient>
    </defs>
    <path d="M0 0 H1200 V90 C900 30 500 40 0 58 Z" fill="url(#topBand)"/>
    <path d="M0 64 C500 46 900 38 1200 98" fill="none" stroke="#b9c3cf" stroke-width="4"/>
  </svg>

  <div class="brand">
    <div class="brand-mark"></div>
    <div class="brand-name">Korbin<br>Lanzer</div>
  </div>

  <div class="doc-kicker">TEMPLATE</div>
  <div class="doc-title">Schulungsunterlagen<br>für IT-SEMINARE</div>

  <div class="slogan">Your <strong>SLOGAN</strong> Here</div>
  <p class="slogan-copy">Sed ut perspiciatis unde omnis iste natus error sit voluptatem accusantium doloremque laudantium, totam rem aperiam, explicabo. Nemo enim ipsam voluptatem quia consequuntur magni dolores eos qui ratione voluptatem sequi nesciunt. Neque porro quisquam est, qui dolorem ipsum quia dolor sit amet, consectetur, tempora incidunt ut labore et dolore magnam aliquam quaerat voluptatem. Ut enim ad minima veniam, quis nostrum exercitationem ullam.</p>

  <div class="hero-art" role="img" aria-label="Illustration: Arbeitsplatz von oben mit Bildschirm, Tastatur, Händen, Kalender, Taschenrechner, Notizzetteln und Klemmbrett"></div>

  <svg class="cover-wave" width="1200" height="472" viewBox="0 0 1200 472">
    <defs>
      <linearGradient id="coverWave" x1="0" y1="0" x2="1" y2="1">
        <stop offset="0" stop-color="#0c2b5c"/>
        <stop offset=".5" stop-color="#1f63ad"/>
        <stop offset="1" stop-color="#5aa8e0"/>
      </linearGradient>
      <linearGradient id="coverShine" x1="0" y1="0" x2="1" y2="0">
        <stop offset="0" stop-color="#ffffff" stop-opacity="0"/>
        <stop offset=".6" stop-color="#ffffff" stop-opacity=".55"/>
        <stop offset="1" stop-color="#ffffff" stop-opacity=".9"/>
      </linearGradient>
    </defs>
    <path d="M0 70 C260 10 600 -10 900 40 C1040 64 1130 110 1200 150 V472 H0 Z" fill="url(#coverWave)"/>
    <path d="M0 420 C400 340 800 330 1200 380 V472 H0 Z" fill="#ffffff" opacity=".12"/>
    <path d="M520 60 C800 70 1000 120 1200 210" fill="none" stroke="url(#coverShine)" stroke-width="10"/>
  </svg>

  <div class="cover-block">
    <h2>BUSINESS</h2>
    <div class="sub">LAYOUT</div>
    <h3>SED UT PERSPICIATIS UNDE SIT AMET</h3>
    <p class="lead">Curabitur at libero est, nec laoreet sapien. Duis rutrum, nisi tristique pharetra.<br>Curabitur at libero est, nec laoreet sapien. Duis rutrum, nisi tristique pharetra, neque.</p>
    <p class="body">Sed ut perspiciatis unde omnis iste natus error sit voluptatem accusantium doloremque laudantium, totam rem aperiam, eaque ipsa quae ab illo inventore veritatis et quasi architecto beatae vitae dicta sunt explicabo. Nemo enim ipsam voluptatem quia voluptas sit aspernatur aut odit aut fugit, sed quia consequuntur magni dolores eos qui ratione voluptatem sequi nesciunt. Neque porro quisquam est, qui dolorem ipsum quia dolor sit amet, consectetur, adipisci velit, sed quia non numquam eius modi tempora incidunt ut labore et dolore magnam aliquam quaerat voluptatem. Ut enim ad minima veniam, quis nostrum exercitationem ullam corporis suscipit laboriosam, nisi ut aliquid ex.</p>
  </div>
</section>

<!-- ================= CONTENTS PAGE ================= -->
<section class="contents">
  <svg class="abs" style="left:0;top:0" width="1200" height="70" viewBox="0 0 1200 70">
    <defs>
      <linearGradient id="pageBand" x1="0" y1="0" x2="1" y2="0">
        <stop offset="0" stop-color="#0c2b5c"/>
        <stop offset=".5" stop-color="#1f63ad"/>
        <stop offset="1" stop-color="#3d96d6"/>
      </linearGradient>
    </defs>
    <path d="M0 0 H1200 V40 C800 20 400 28 0 50 Z" fill="url(#pageBand)"/>
  </svg>

  <div class="brand">
    <div class="brand-mark"></div>
    <div class="brand-name">Korbin<br>Lanzer</div>
  </div>

  <h1 class="toc-title">Inhaltsverzeichnis</h1>

  <div class="section-art" role="img" aria-label="Illustration: Laptop mit Liniendiagramm und Lupe"></div>
  <div class="section-rule"></div>
  <h2 class="section-head">SED UT PERSPICIATIS UNDE SIT AMET</h2>
  <p class="section-text">Lorem ipsum dolor sit amet, consectetuer adipiscing elit. Aenean commodo ligula eget dolor. Aenean massa. Cum sociis natoque penatibus et magnis dis parturient montes, nascetur ridiculus mus. Donec quam felis, ultricies nec, pellentesque eu, pretium quis, sem. Nulla consequat massa quis enim. Donec pede justo, fringilla vel, aliquet nec, vulputate eget, arcu. In enim justo, rhoncus ut, imperdiet a, venenatis vitae, justo. Nullam dictum felis eu pede mollis pretium. Integer tincidunt. Cras dapibus. Vivamus elementum semper nisi. Aenean vulputate eleifend tellus. Aenean leo ligula, porttitor eu, consequat vitae, eleifend ac, enim. Aliquam lorem ante, dapibus in, viverra quis, feugiat a, tellus. Phasellus viverra nulla ut metus varius laoreet. Quisque rutrum. Aenean imperdiet. Etiam ultricies nisi vel augue. Curabitur ullamcorper ultricies nisi. Nam eget dui. Etiam rhoncus. Maecenas tempus, tellus eget condimentum rhoncus, sem quam semper libero, sit amet adipiscing sem neque sed ipsum. Nam quam nunc, blandit vel, luctus pulvinar, hendrerit id, lorem. Maecenas nec odio et ante tincidunt tempus. Donec vitae sapien ut libero venenatis faucibus. Nullam quis ante. Etiam sit amet orci eget eros faucibus tincidunt. Duis leo. Sed fringilla mauris sit amet nibh. Donec sodales sagittis magna. Sed consequat, leo eget bibendum sodales, augue velit cursus nunc, quis gravida magna mi a libero. Fusce vulputate eleifend sapien. Vestibulum purus quam, scelerisque ut, mollis sed, nonummy id, metus. Nullam accumsan lorem in dui. Cras ultricies mi eu turpis hendrerit fringilla. Vestibulum ante ipsum primis in faucibus orci luctus et ultrices posuere cubilia Curae; in ac dui quis mi consectetuer lacinia. Nam pretium turpis et arcu. Duis arcu tortor, suscipit eget, imperdiet nec, imperdiet iaculis, ipsum. Sed aliquam ultrices mauris. Integer ante arcu, accumsan a, consectetuer eget, posuere ut, mauris. Praesent adipiscing. Phasellus ullamcorper ipsum rutrum nunc. Nunc nonummy metus. Vestibulum volutpat pretium libero. Cras id dui. Aenean ut.</p>

  <div class="topic" style="left:140px">
    <div class="topic-icon" role="img" aria-label="Symbol: Lupe über Dokument" style="background:#e8623a"></div>
    <h4>ADD SOME TEXT &amp; DATA</h4>
    <p>Lorem ipsum dolor sit amet, commodo et, tristique urna lorem sed pellentesque morbi leo curabitur</p>
  </div>
  <div class="topic" style="left:475px">
    <div class="topic-icon" role="img" aria-label="Symbol: Bildschirm mit Zahnrad" style="background:#2c4a70"></div>
    <h4>ADD SOME TEXT &amp; DATA</h4>
    <p>Lorem ipsum dolor sit amet, commodo et, tristique urna lorem sed pellentesque morbi leo curabitur ipsum dolor</p>
  </div>
  <div class="topic" style="left:810px">
    <div class="topic-icon" role="img" aria-label="Symbol: Zielscheibe mit Diagramm" style="background:#f08a2c"></div>
    <h4>ADD SOME TEXT &amp; DATA</h4>
    <p>Lorem ipsum dolor sit amet, commodo et, tristique urna lorem sed pellentesque morbi leo curabitur</p>
  </div>

  <div class="tag tag-teal">PLACE YOUR TEXT HERE</div>
  <div class="tag tag-navy">SED UT PERSPICIATIS UNDE SIT AMET</div>

  <svg class="abs" style="left:0;top:1530px" width="1200" height="90" viewBox="0 0 1200 90">
    <path d="M0 44 C400 24 800 22 1200 4 V90 H0 Z" fill="url(#pageBand)"/>
    <path d="M0 38 C400 18 800 16 1200 -2" fill="none" stroke="#b9c3cf" stroke-width="3"/>
  </svg>
</section>

</body>
</html>
```